Authentic Log Lodge Requires Highway Signage (x2)

We are recently established Lodge and Cabins in Golden, BC, Canada. We already have a great reputation and have recently achieved a Wander Scout Badge of Merit - our guests love us and we love them.

Quillan Lodge is looking for two new signs;
1 - A highway sign (8ft high, 12ft wide) and a secondary directional sign (approx 3ft square). We have a strong brand and imagery and can supply photos and vectors. We are currently fighting an internal battle of how the highway sign should look - one option includes an image of the Lodge and the other is based around our logo. The design must include two items of text - "www.quillanlodge-example.com" and "Next Right"

2 - A directional sign. We would like this sign to be logo based and include a right facing arrow. The size of this sign can be flexible.

It would be great to establish a relationship with someone for future work.

We are in desperate need of some creative geniuses to don their superhero capes and come to our rescue.

Target Market(s)

Current guests looking to find us and prospective guests driving along the highway.

Industry/Entity Type

Hospitality

Font styles to use
Sans Serif

Colors

Designer to choose colors to be used in the design.

Requirements
Must have
• It must contain our logo and maintain the feel of our brand.
• It must be based on the brand colours (see attached documents).

```html
<!DOCTYPE html>
<html lang="en">
<head>
<meta charset="utf-8">
<title>Quillan Lodge – Directional Sign</title>
<link href="https://fonts.googleapis.com/css2?family=Jost:wght@600;700&display=swap" rel="stylesheet">
<style>
  :root {
    --log-light: #e2c596;
    --log-mid: #c9a36b;
    --log-dark: #2b2620;
    --plate-grey: #7a7068;
    --brand-green: #b3bb2b;
    --cream: #fdf9e6;
    --banner-red: #8f1e22;
    --banner-red-dark: #7a171b;
  }
  html, body {
    margin: 0;
    padding: 0;
    width: 1200px;
    height: 1200px;
    overflow: hidden;
    background: var(--log-dark);
  }
  .sign {
    position: relative;
    width: 1200px;
    height: 1200px;
    overflow: hidden;
    font-family: "Jost", "Futura", sans-serif;
  }
  .log-stack {
    position: absolute;
    inset: 0;
    background:
      radial-gradient(circle at 30% 25%, var(--log-light) 0%, var(--log-mid) 55%, #9c7a4c 100%);
  }
  .name-plate {
    position: absolute;
    left: 214px;
    top: 180px;
    width: 774px;
    height: 660px;
    background: var(--plate-grey);
    border-radius: 28px;
    box-shadow: 0 10px 30px rgba(0, 0, 0, 0.35);
  }
  .lodge-name {
    position: absolute;
    left: 0;
    right: 0;
    top: 175px;
    margin: 0;
    text-align: center;
    color: var(--brand-green);
    font-weight: 700;
    line-height: 1.15;
  }
  .lodge-name .primary {
    display: block;
    font-size: 100px;
    letter-spacing: 0.12em;
    padding-left: 0.12em;
  }
  .lodge-name .secondary {
    display: block;
    font-size: 70px;
    letter-spacing: 0.2em;
    padding-left: 0.2em;
  }
  .location {
    position: absolute;
    left: 0;
    right: 0;
    top: 420px;
    margin: 0;
    text-align: center;
    color: var(--cream);
    font-weight: 600;
    font-size: 29px;
    letter-spacing: 0.2em;
    padding-left: 0.2em;
  }
  .direction-arrow {
    position: absolute;
    left: 176px;
    top: 990px;
    width: 860px;
    height: 160px;
    filter: drop-shadow(0 6px 10px rgba(0, 0, 0, 0.35));
  }
  .direction-label {
    position: absolute;
    left: 176px;
    top: 1014px;
    width: 800px;
    height: 104px;
    margin: 0;
    display: flex;
    align-items: center;
    justify-content: center;
    color: var(--cream);
    font-weight: 700;
    font-size: 78px;
    letter-spacing: 0.14em;
  }
</style>
</head>
<body>
  <main class="sign">
    <div class="log-stack" role="img" aria-label="Photograph of stacked cut log ends"></div>

    <section class="name-plate">
      <h1 class="lodge-name">
        <span class="primary">QUILLAN</span>
        <span class="secondary">LODGE</span>
      </h1>
      <p class="location">GOLDEN - BRITISH COLUMBIA</p>
    </section>

    <svg class="direction-arrow" viewBox="0 0 860 160" aria-hidden="true">
      <polygon points="0,24 808,24 808,0 856,80 808,160 808,128 0,128 18,76"
               fill="var(--banner-red)"/>
      <polygon points="18,76 808,76 808,128 0,128"
               fill="var(--banner-red-dark)" opacity="0.6"/>
    </svg>
    <p class="direction-label">NEXT RIGHT</p>
  </main>
</body>
</html>
```